Review/Re-Design Supermarket E-Commerce website

We have launched our Supermarket E-commerce Website but feel it is lacking a modern feel.

Please re-design the current Supermarket E-commerce site, creating a more modern look and feel.

I am looking for design changes to things such as:

- Fonts
- Button shape & Size
- Shapes of boxes
- Layout of drop down menus
- A new shopping cart / button
- The Header (and in particular the use and positioning of the logo)
- Supplying a generic background image (currently berries)

Please do not change the structure of the page. For instance, the category selection will always be on the left, the items will always be displayed in rows of 3 and the shopping cart should be on the right.
Updates

Current site can be found at www.korvamarketplace.com.au

Project Deadline Extended
Reason: designs coming in are generally too different from current design. we are looking for less that 10% change to the overall look and feel. one aspect that needs a lot of work is the checkout cart on the right hand side. please checkout http://www2.pellingtonfresh.com.au/?gclid=XQWB4pzrhnLDGAKUrTmeYbNVsP

Target Market(s)

Consumers buying their weekly grocery shopping online

Industry/Entity Type

Shopping

Number of Pages Required

1 page

Requirements
Must have
• Stick to the branding of the Logo. Which is Red, Blue and White.
• Other colours may be used in small percentages.
Should not have
• Do not change the Structure of the site.

```html
<!DOCTYPE html>
<html lang="en">
<head>
<meta charset="utf-8">
<title>Korva Marketplace – Apples</title>
<link href="https://fonts.googleapis.com/css2?family=Open+Sans:wght@400;600;700&display=swap" rel="stylesheet">
<style>
:root{
  --blue:#0a5bab;
  --blue-dark:#084a8c;
  --red:#e31b23;
  --yellow:#ffcc00;
  --text:#333;
  --muted:#666;
  --line:#e3e3e3;
  --panel:#ececec;
  --panel-light:#f4f4f4;
  --white:#fff;
  --footer-bar:#6d6d6d;
}
*{box-sizing:border-box;margin:0;padding:0}
html,body{width:930px;height:1200px;overflow:hidden}
body{font-family:'Open Sans',sans-serif;color:var(--text);position:relative;font-size:11px}
.backdrop{position:absolute;inset:0;background:linear-gradient(90deg,#7a3a22 0%,#b0442f 2%,#8a4a2c 4.5%,#fff 4.5%,#fff 95.9%,#8a4a2c 95.9%,#b0442f 98%,#7a3a22 100%)}
.page{position:absolute;left:42px;top:0;width:850px;height:1200px;background:var(--white)}
.abs{position:absolute}
/* top bar */
.topbar{left:0;top:0;width:850px;height:28px;background:var(--blue);color:var(--white);font-size:10px}
.topbar .phone{left:14px;top:7px;display:flex;align-items:center;gap:8px}
.topbar nav{right:126px;top:8px;display:flex;gap:16px;font-weight:700}
.cart-tab{right:0;top:0;width:97px;height:28px;background:var(--red);display:flex;align-items:center;justify-content:center;gap:5px;font-weight:700}
.cart-tab .count{background:#0f8a3c;border-radius:50%;width:14px;height:14px;font-size:9px;display:flex;align-items:center;justify-content:center}
/* brand */
.brand{left:0;width:850px;top:58px;text-align:center}
.brand .name{font-size:19px;font-weight:700;color:var(--blue);letter-spacing:.5px}
.brand .sub{font-size:9px;letter-spacing:5px;color:var(--muted)}
/* search */
.search{left:29px;top:114px;width:795px;height:51px;background:var(--panel);border:1px solid #d6d6d6}
.search .label{left:16px;top:14px;font-size:17px;color:#555}
.field{top:14px;height:23px;background:var(--white);border:1px solid #d0d0d0;font-size:10px;color:#999;padding:4px 7px;display:flex;justify-content:space-between;align-items:center}
.field.dark{color:var(--text)}
.search .go{left:654px;top:14px;width:107px;height:21px;background:var(--blue);color:var(--white);font-weight:700;font-size:10px;display:flex;align-items:center;justify-content:center;gap:6px}
/* sidebar */
.sidebar{left:29px;top:180px;width:173px}
.side-item{height:30px;border:1px solid var(--line);border-top:none;padding:0 9px;display:flex;align-items:center;justify-content:space-between;font-size:10px;background:var(--white)}
.side-item.cat{height:32px;font-size:12px;background:#fafafa}
.side-item.specials{height:28px;background:var(--blue);color:var(--white);font-size:12px;border:none}
.side-item.favs{height:29px;background:var(--yellow);font-size:12px;border:none}
.side-item.open{height:32px;color:var(--blue);font-weight:700;font-size:12px}
.badge{width:18px;height:18px;border-radius:50%;background:var(--white);display:flex;align-items:center;justify-content:center;font-weight:700;font-size:11px}
/* breadcrumb */
.crumbs{left:223px;top:178px;font-size:10px}
.crumbs span{color:#aaa;margin:0 3px}
.crumb-line{left:225px;top:203px;width:443px;height:1px;background:var(--line)}
/* grid */
.grid{left:225px;top:218px;width:446px;display:grid;grid-template-columns:repeat(3,1fr)}
.product{height:248px;border-right:1px solid var(--line);border-bottom:1px solid var(--line);position:relative;overflow:hidden}
.product:nth-child(n+7){border-bottom:none}
.photo{position:absolute;left:50%;top:18px;transform:translateX(-50%);width:78px;height:78px;border-radius:50%;background:radial-gradient(circle at 35% 35%,#f0566a,#b8142a 70%)}
.photo.wide{width:110px;height:98px;top:10px;border-radius:45%}
.photo.green{background:radial-gradient(circle at 35% 35%,#9fe05a,#3d9b1c 70%)}
.photo.mixed{background:radial-gradient(circle at 35% 35%,#f4c25a,#d94a2c 75%)}
.photo.yellow{background:radial-gradient(circle at 35% 35%,#fbe08a,#d7a531 75%)}
.photo.lime{background:radial-gradient(circle at 35% 35%,#e2ef8a,#a9c63a 75%)}
.photo.small{width:64px;height:64px;top:30px}
.pname{position:absolute;left:0;right:0;top:136px;text-align:center;color:var(--blue);font-weight:600;font-size:13px;line-height:16px}
.buy{position:absolute;left:3px;top:186px;width:140px;height:51px;display:flex;gap:3px}
.price-box{width:75px;background:var(--panel-light);position:relative}
.price{position:absolute;left:6px;top:3px;font-size:14px;font-weight:600;color:#555}
.each{position:absolute;left:6px;top:20px;font-size:8px;color:#777}
.qty{position:absolute;left:2px;right:2px;bottom:2px;height:14px;display:flex;justify-content:space-between;align-items:center;font-size:10px;background:#e9e9e9}
.qty b{width:13px;height:13px;background:var(--white);border:1px solid #999;display:flex;align-items:center;justify-content:center;font-size:10px}
.add{width:62px;background:var(--red);color:var(--white);text-align:center;font-weight:700;line-height:1}
.add small{display:block;font-size:9px;margin-top:10px}
.add strong{display:block;font-size:17px;margin-top:3px}
.loading{left:225px;top:962px;width:443px;height:25px;background:var(--panel);font-size:11px;display:flex;align-items:center;justify-content:center;gap:8px;color:#555}
/* cart panel */
.cart{left:679px;top:203px;width:145px;height:234px;background:var(--panel-light);border:1px solid var(--line)}
.cart-head{height:26px;background:var(--blue);color:var(--white);font-weight:700;font-size:10px;display:flex;align-items:center;gap:8px;padding:0 7px}
.cart .addr{height:44px;padding:8px 11px;font-size:10px;line-height:14px}
.cart .items{height:53px;display:flex;align-items:center;gap:14px;padding:0 12px;font-size:14px;color:#555;border-bottom:1px solid var(--line)}
.cart .total{padding:12px 13px;display:flex;justify-content:space-between;align-items:center;font-size:12px}
.cart .total strong{color:var(--red);font-size:15px}
.checkout{margin:4px 0 0 16px;width:110px;height:21px;display:flex;background:var(--blue);color:var(--white);font-weight:700;font-size:10px}
.checkout .tick{width:25px;background:var(--yellow);display:flex;align-items:center;justify-content:center}
.checkout span{flex:1;display:flex;align-items:center;justify-content:center}
/* footer */
.footer{left:0;top:1026px;width:850px;height:136px;display:flex;border-top:1px solid #ddd}
.fcol{padding:26px 22px;font-size:10px}
.fcol li{list-style:none;display:flex;align-items:center;gap:8px;height:21.5px}
.fcol:nth-child(1){width:202px;background:var(--panel-light)}
.fcol:nth-child(2){width:186px;background:var(--white);padding-left:30px}
.fcol:nth-child(3){width:187px;background:var(--panel-light);padding-left:26px}
.fcol:nth-child(4){flex:1;background:var(--white);display:flex;gap:20px;padding:14px 19px}
.fcol h4{color:var(--blue);font-size:12px;font-weight:600;margin-bottom:8px}
.appbtn{width:113px;height:38px;border-radius:5px;background:#111;color:var(--white);display:flex;align-items:center;gap:6px;padding:0 8px;line-height:1.05;margin-bottom:6px}
.appbtn.light{background:var(--white);color:#111;border:2px solid #111}
.appbtn em{font-style:normal;font-size:8px;display:block}
.appbtn strong{font-weight:400;font-size:15px}
.card{display:inline-block;width:36px;height:23px;border-radius:2px;margin-right:4px}
.seal{width:30px;height:30px;border-radius:50%;background:#c9a63a;border:2px solid #8a6d18;margin-top:6px}
.bottom{left:0;top:1162px;width:850px;height:38px;background:var(--footer-bar);color:var(--white);font-size:10px;display:flex;justify-content:space-between;align-items:center;padding:0 18px}
svg{display:block}
</style>
</head>
<body>
<div class="backdrop" role="img" aria-label="Background photograph of red cherries scattered on dark wooden boards"></div>
<div class="page">
  <header class="topbar abs">
    <div class="phone abs"><svg width="10" height="10" viewBox="0 0 24 24"><path fill="#fff" d="M6.6 10.8a15 15 0 006.6 6.6l2.2-2.2a1 1 0 011-.25 11.4 11.4 0 003.6.57 1 1 0 011 1V20a1 1 0 01-1 1A17 17 0 013 4a1 1 0 011-1h3.5a1 1 0 011 1c0 1.25.2 2.45.57 3.57a1 1 0 01-.25 1z"/></svg>1300 555 019</div>
    <nav class="abs"><span>PRODUCTS</span><span>LOGIN</span><span>REGISTER</span></nav>
    <div class="cart-tab abs"><svg width="12" height="11" viewBox="0 0 24 22"><path fill="none" stroke="#fff" stroke-width="2.4" d="M1 2h4l3 12h12l3-9H7"/><circle cx="10" cy="19" r="2" fill="#fff"/><circle cx="19" cy="19" r="2" fill="#fff"/></svg>MY CART <span class="count">6</span></div>
  </header>

  <div class="brand abs">
    <div class="name">KORVA MARKETPLACE</div>
    <div class="sub">SUPERMARKETS</div>
  </div>

  <section class="search abs">
    <div class="label abs">Search Products</div>
    <div class="field abs" style="left:171px;width:240px">Search for Products, Category or Brand</div>
    <div class="field abs dark" style="left:419px;width:108px">Filter by <svg width="10" height="6" viewBox="0 0 10 6"><path d="M1 1l4 4 4-4" fill="none" stroke="#888"/></svg></div>
    <div class="field abs dark" style="left:538px;width:108px">Sort <svg width="10" height="6" viewBox="0 0 10 6"><path d="M1 1l4 4 4-4" fill="none" stroke="#888"/></svg></div>
    <div class="go abs"><svg width="11" height="11" viewBox="0 0 12 12"><circle cx="5" cy="5" r="3.8" fill="none" stroke="#fff" stroke-width="1.6"/><path d="M8 8l3 3" stroke="#fff" stroke-width="1.8"/></svg>SEARCH</div>
  </section>

  <aside class="sidebar abs">
    <div class="side-item specials">Online Specials <span class="badge" style="color:var(--red)">$</span></div>
    <div class="side-item favs">Favourites <span class="badge" style="background:#fff"><svg width="11" height="11" viewBox="0 0 24 24"><path fill="#ffcc00" d="M12 2l3 6.9 7.5.7-5.7 5 1.7 7.4L12 18l-6.5 4 1.7-7.4-5.7-5 7.5-.7z"/></svg></span></div>
    <div class="side-item open">Baby <svg width="10" height="6" viewBox="0 0 10 6"><path d="M1 5l4-4 4 4" fill="none" stroke="#999"/></svg></div>
    <div class="side-item">Accessories</div>
    <div class="side-item">Baby Food</div>
    <div class="side-item">Baby Oil</div>
    <div class="side-item">Bath Time</div>
    <div class="side-item">Change Time</div>
    <div class="side-item">Cleaning</div>
    <div class="side-item">Creams &amp; Ointments</div>
    <div class="side-item">Feeding Time</div>
    <div class="side-item">Formula</div>
    <div class="side-item cat">Bakery <svg width="10" height="6" viewBox="0 0 10 6"><path d="M1 1l4 4 4-4" fill="none" stroke="#999"/></svg></div>
    <div class="side-item cat">Baking Needs <svg width="10" height="6" viewBox="0 0 10 6"><path d="M1 1l4 4 4-4" fill="none" stroke="#999"/></svg></div>
    <div class="side-item cat">Beverages <svg width="10" height="6" viewBox="0 0 10 6"><path d="M1 1l4 4 4-4" fill="none" stroke="#999"/></svg></div>
    <div class="side-item cat">Biscuits <svg width="10" height="6" viewBox="0 0 10 6"><path d="M1 1l4 4 4-4" fill="none" stroke="#999"/></svg></div>
    <div class="side-item cat">Breakfast Foods <svg width="10" height="6" viewBox="0 0 10 6"><path d="M1 1l4 4 4-4" fill="none" stroke="#999"/></svg></div>
    <div class="side-item cat">Canned Food <svg width="10" height="6" viewBox="0 0 10 6"><path d="M1 1l4 4 4-4" fill="none" stroke="#999"/></svg></div>
    <div class="side-item cat">Cheese <svg width="10" height="6" viewBox="0 0 10 6"><path d="M1 1l4 4 4-4" fill="none" stroke="#999"/></svg></div>
    <div class="side-item cat">Chilled Foods <svg width="10" height="6" viewBox="0 0 10 6"><path d="M1 1l4 4 4-4" fill="none" stroke="#999"/></svg></div>
    <div class="side-item cat">Desserts <svg width="10" height="6" viewBox="0 0 10 6"><path d="M1 1l4 4 4-4" fill="none" stroke="#999"/></svg></div>
    <div class="side-item cat">Fruit <svg width="10" height="6" viewBox="0 0 10 6"><path d="M1 1l4 4 4-4" fill="none" stroke="#999"/></svg></div>
  </aside>

  <div class="crumbs abs">Home<span>/</span>Fruit<span>/</span>Apples</div>
  <div class="crumb-line abs"></div>

  <main class="grid abs">
    <article class="product"><div class="photo wide" role="img" aria-label="Photo of a bag of red apples"></div><h3 class="pname">Apples Red<br>2kg Bag</h3><div class="buy"><div class="price-box"><span class="price">$8.39</span><span class="each">$8.39 ea</span><div class="qty"><b>−</b>2<b>+</b></div></div><div class="add"><small>ADD TO</small><strong>CART</strong></div></div></article>
    <article class="product"><div class="photo mixed small" role="img" aria-label="Photo of a single Fuji apple"></div><h3 class="pname">Fuji Apples Each</h3><div class="buy"><div class="price-box"><span class="price">$8.39</span><span class="each">$8.39 ea</span><div class="qty"><b>−</b>2<b>+</b></div></div><div class="add"><small>ADD TO</small><strong>CART</strong></div></div></article>
    <article class="product"><div class="photo green" role="img" aria-label="Photo of a green apple with a leaf"></div><h3 class="pname">Green Apples Each</h3><div class="buy"><div class="price-box"><span class="price">$8.39</span><span class="each">$8.39 ea</span><div class="qty"><b>−</b>2<b>+</b></div></div><div class="add"><small>ADD TO</small><strong>CART</strong></div></div></article>
    <article class="product"><div class="photo small" role="img" aria-label="Photo of a red apple"></div><h3 class="pname">Rosy Crisp<br>Apples Each</h3><div class="buy"><div class="price-box"><span class="price">$8.39</span><span class="each">$8.39 ea</span><div class="qty"><b>−</b>2<b>+</b></div></div><div class="add"><small>ADD TO</small><strong>CART</strong></div></div></article>
    <article class="product"><div class="photo mixed small" role="img" aria-label="Photo of a red and yellow gala apple"></div><h3 class="pname">Royal Gala<br>Apples Each</h3><div class="buy"><div class="price-box"><span class="price">$8.39</span><span class="each">$8.39 ea</span><div class="qty"><b>−</b>2<b>+</b></div></div><div class="add"><small>ADD TO</small><strong>CART</strong></div></div></article>
    <article class="product"><div class="photo wide lime" role="img" aria-label="Photo of a pile of yellow-green apples with slices"></div><h3 class="pname">Yellow Apples<br>1.5kg Bag</h3><div class="buy"><div class="price-box"><span class="price">$8.39</span><span class="each">$8.39 ea</span><div class="qty"><b>−</b>2<b>+</b></div></div><div class="add"><small>ADD TO</small><strong>CART</strong></div></div></article>
    <article class="product"><div class="photo yellow small" role="img" aria-label="Photo of a yellow apple"></div><h3 class="pname" style="top:144px">Yellow Apples Each</h3><div class="buy"><div class="price-box"><span class="price">$8.39</span><span class="each">$8.39 ea</span><div class="qty"><b>−</b>2<b>+</b></div></div><div class="add"><small>ADD TO</small><strong>CART</strong></div></div></article>
    <article class="product"><div class="photo mixed small" role="img" aria-label="Photo of a red and yellow apple"></div><h3 class="pname" style="top:144px">Yellow Apples Each</h3><div class="buy"><div class="price-box"><span class="price">$8.39</span><span class="each">$8.39 ea</span><div class="qty"><b>−</b>2<b>+</b></div></div><div class="add"><small>ADD TO</small><strong>CART</strong></div></div></article>
    <article class="product"><div class="photo small" role="img" aria-label="Photo of a red apple"></div><h3 class="pname" style="top:144px">Yellow Apples Each</h3><div class="buy"><div class="price-box"><span class="price">$8.39</span><span class="each">$8.39 ea</span><div class="qty"><b>−</b>2<b>+</b></div></div><div class="add"><small>ADD TO</small><strong>CART</strong></div></div></article>
  </main>

  <div class="loading abs">Loading more results <svg width="11" height="11" viewBox="0 0 12 12"><circle cx="6" cy="6" r="4.5" fill="none" stroke="#333" stroke-width="1.5" stroke-dasharray="2 2"/></svg></div>

  <aside class="cart abs">
    <div class="cart-head"><svg width="13" height="13" viewBox="0 0 14 14"><rect x="2" y="3" width="10" height="10" fill="#fff"/><path d="M4 3V1h6v2" fill="none" stroke="#fff" stroke-width="1.4"/></svg>CLICK &amp; COLLECT</div>
    <div class="addr">4/12-18 Marlow Street<br>Brackenfield TAS 7299</div>
    <div class="cart-head"><svg width="15" height="12" viewBox="0 0 16 12"><rect x="0" y="2" width="9" height="7" fill="#fff"/><path d="M9 4h4l3 3v2H9z" fill="#fff"/><circle cx="3.5" cy="10" r="1.8" fill="#fff"/><circle cx="12.5" cy="10" r="1.8" fill="#fff"/></svg>DELIVERY INFO</div>
    <div class="items"><svg width="24" height="22" viewBox="0 0 24 22"><path fill="none" stroke="#0a5bab" stroke-width="2.4" d="M1 2h4l3 12h12l3-9H7"/><circle cx="10" cy="19" r="2" fill="#0a5bab"/><circle cx="19" cy="19" r="2" fill="#0a5bab"/></svg>6 Items</div>
    <div class="total">Sub Total <strong>$24.00</strong></div>
    <div class="checkout"><div class="tick"><svg width="12" height="10" viewBox="0 0 12 10"><path d="M1 5l3.5 3.5L11 1" fill="none" stroke="#0a5bab" stroke-width="2"/></svg></div><span>CHECKOUT</span></div>
  </aside>

  <footer class="footer abs">
    <ul class="fcol">
      <li><svg width="10" height="10" viewBox="0 0 10 10"><circle cx="5" cy="3" r="2.4" fill="#0a5bab"/><path d="M1 10a4 4 0 018 0z" fill="#0a5bab"/></svg>My Account</li>
      <li><svg width="10" height="10" viewBox="0 0 10 10"><circle cx="5" cy="5.5" r="3.8" fill="none" stroke="#0a5bab" stroke-width="1.3"/><path d="M5 3.5v2h1.5" stroke="#0a5bab" fill="none"/></svg>My Past Orders</li>
      <li><span style="color:var(--red);font-weight:700;width:10px">$</span>Online Specials</li>
      <li><svg width="10" height="10" viewBox="0 0 10 10"><rect x="1" y="2" width="8" height="7" fill="none" stroke="#0a5bab"/><path d="M1 4h8" stroke="#0a5bab"/></svg>Everyday Special</li>
    </ul>
    <ul class="fcol">
      <li><svg width="10" height="10" viewBox="0 0 12 10"><path d="M1 5l3.5 3.5L11 1" fill="none" stroke="#0a5bab" stroke-width="2"/></svg>About Tillway</li>
      <li><svg width="10" height="10" viewBox="0 0 10 10"><circle cx="5" cy="3" r="2.2" fill="none" stroke="#0a5bab"/><path d="M1.5 9.5a3.5 3.5 0 017 0z" fill="none" stroke="#0a5bab"/></svg>About Us</li>
      <li><svg width="10" height="10" viewBox="0 0 10 10"><rect x="0.5" y="2" width="9" height="6" fill="#0a5bab"/><path d="M0.5 2L5 5.5 9.5 2" stroke="#fff" fill="none"/></svg>Contact Us</li>
      <li><svg width="10" height="10" viewBox="0 0 24 24"><path fill="#0a5bab" d="M6.6 10.8a15 15 0 006.6 6.6l2.2-2.2a1 1 0 011-.25 11.4 11.4 0 003.6.57 1 1 0 011 1V20a1 1 0 01-1 1A17 17 0 013 4a1 1 0 011-1h3.5a1 1 0 011 1c0 1.25.2 2.45.57 3.57a1 1 0 01-.25 1z"/></svg>1300 555 019</li>
    </ul>
    <ul class="fcol">
      <li><svg width="11" height="9" viewBox="0 0 16 12"><rect x="0" y="2" width="9" height="7" fill="#0a5bab"/><path d="M9 4h4l3 3v2H9z" fill="#0a5bab"/></svg>Delivery</li>
      <li><span style="color:var(--blue);font-weight:700;width:10px">?</span>FAQ</li>
      <li><svg width="10" height="10" viewBox="0 0 10 10"><path d="M2 9l5-5M6 1l3 3-2 1-2-2z" stroke="#0a5bab" stroke-width="1.6" fill="#0a5bab"/></svg>Privacy Policy</li>
      <li><svg width="10" height="10" viewBox="0 0 10 10"><path d="M1 9l1-3 5-5 2 2-5 5z" fill="#0a5bab"/></svg>Terms &amp; Conditions</li>
    </ul>
    <div class="fcol">
      <div>
        <h4>Download Our Apps</h4>
        <div class="appbtn"><svg width="12" height="20" viewBox="0 0 12 20"><rect x="1" y="1" width="10" height="18" rx="2" fill="none" stroke="#fff" stroke-width="1.5"/></svg><div><em>Available on the</em><strong>App Stores</strong></div></div>
        <div class="appbtn light"><svg width="12" height="20" viewBox="0 0 12 20"><rect x="1" y="1" width="10" height="18" rx="2" fill="none" stroke="#111" stroke-width="1.5"/></svg><div style="font-size:11px">Mobile site<br>Available</div></div>
      </div>
      <div>
        <h4>We Accept</h4>
        <span class="card" style="background:#d8d8d8"></span><span class="card" style="background:#c9d2e6"></span>
        <div class="seal"></div>
      </div>
    </div>
  </footer>
  <div class="bottom abs"><span>© Tillway Pty Ltd 2014 - All Rights Reserved</span><span>End User License Agreement</span></div>
</div>
</body>
</html>
```